Young Adult novel ebook design

The book is called Label Whore: Inspired By A True StoryIt's about a wealthy male teenager who is too much into appearances, but is later humbled by a seriea of events. I need a trendy cover that resembles other top Young Adult covers, such as the examples attached. But something unique that stands out.
Target Market(s)
Teens, young adult, middle schoolers, high schoolers
Industry/Entity Type
Writer
Colors
Designer to choose colors to be used in the design.
Requirements
Must have
- Be creative and eye catching for a teenager. Leave space for the author's name. Will reveal the name to the winner.
Nice to have
- Get inspired by some of the example covers I attached.
Should not have
- No images that clearly shows a person's race. The main character image should be up for interpretation.

```html
<!DOCTYPE html>
<html lang="en">
<head>
<meta charset="utf-8">
<title>Velvet Mirror – Cover Options</title>
<link href="https://fonts.googleapis.com/css2?family=Oswald:wght@300;400;500;600&display=swap" rel="stylesheet">
<style>
  :root {
    --board: #a8692f;
    --navy-deep: #05081f;
    --navy-mid: #1c2744;
    --navy-mist: #8d9db4;
    --corridor-light: #f2f5f8;
    --charcoal: #0a0a0a;
    --skin-grey: #b9b9b9;
    --coat-grey: #3b3b3b;
    --type-light: #d8d8da;
    --type-white: #f1f1f1;
    --label-cream: #f6eee2;
  }
  * { margin: 0; padding: 0; box-sizing: border-box; }
  html, body { width: 1200px; height: 900px; overflow: hidden; }
  body {
    background: var(--board);
    position: relative;
    font-family: "Oswald", "Arial Narrow", sans-serif;
  }
  .cover {
    position: absolute;
    overflow: hidden;
    text-align: center;
  }
  .cover--silhouette { left: 42px; top: 48px; width: 540px; height: 757px; background: var(--navy-deep); }
  .cover--portrait { left: 627px; top: 44px; width: 543px; height: 761px; background: var(--charcoal); }

  .cover__art { position: absolute; left: 0; top: 0; width: 100%; height: 100%; }

  /* backlit corridor: bright doorway top centre, misty walls, dark floor */
  .cover--silhouette .cover__art {
    background:
      radial-gradient(ellipse 26% 22% at 50% 14%, var(--corridor-light) 0%, #dfe6ee 45%, rgba(200,212,226,0) 100%),
      radial-gradient(ellipse 12% 40% at 12% 30%, rgba(141,157,180,0.55) 0%, rgba(141,157,180,0) 100%),
      radial-gradient(ellipse 12% 40% at 88% 30%, rgba(141,157,180,0.55) 0%, rgba(141,157,180,0) 100%),
      radial-gradient(ellipse 50% 35% at 50% 25%, rgba(120,138,165,0.7) 0%, rgba(40,52,85,0) 100%),
      linear-gradient(180deg, var(--navy-mid) 0%, #121a36 38%, var(--navy-deep) 58%, var(--navy-deep) 100%);
  }
  .cover__shade {
    position: absolute; left: 0; right: 0; top: 0; height: 100%;
    background: radial-gradient(ellipse 24% 38% at 50% 38%, rgba(5,8,31,0.95) 0%, rgba(5,8,31,0.7) 55%, rgba(5,8,31,0) 100%);
  }

  /* portrait: lit face area top left-centre, leather coat mid greys right, deep black base */
  .cover--portrait .cover__art {
    background:
      radial-gradient(ellipse 30% 22% at 40% 10%, #d6d6d6 0%, var(--skin-grey) 35%, rgba(120,120,120,0) 100%),
      radial-gradient(ellipse 18% 14% at 66% 6%, rgba(200,200,200,0.8) 0%, rgba(200,200,200,0) 100%),
      radial-gradient(ellipse 40% 35% at 72% 42%, var(--coat-grey) 0%, rgba(40,40,40,0.6) 50%, rgba(10,10,10,0) 100%),
      radial-gradient(ellipse 35% 25% at 25% 52%, rgba(55,55,55,0.8) 0%, rgba(10,10,10,0) 100%),
      linear-gradient(180deg, #1a1a1a 0%, #141414 50%, var(--charcoal) 80%);
  }

  .cover__title {
    position: absolute;
    left: 0; right: 0;
    color: var(--type-light);
    line-height: 1;
    text-transform: uppercase;
  }
  .cover__title-top {
    top: 386px; font-size: 140px; font-weight: 400; letter-spacing: -3px;
    transform: scaleX(0.84);
  }
  .cover__title-bottom {
    top: 515px; font-size: 88px; font-weight: 600; letter-spacing: -1px;
    transform: scaleX(0.92);
  }

  .cover__tagline {
    position: absolute; left: 0; right: 0; top: 606px;
    color: var(--type-white);
    font-size: 23px; font-weight: 300; letter-spacing: 1.8px;
  }
  .cover__author {
    position: absolute; left: 0; right: 0; top: 686px;
    color: var(--type-white);
    font-size: 30px; font-weight: 300; letter-spacing: 2px;
  }

  .option-label {
    position: absolute; top: 826px;
    color: var(--label-cream);
    font-size: 31px; font-weight: 300; letter-spacing: 1.5px;
    width: 200px; text-align: center;
  }
  .option-label--one { left: 186px; }
  .option-label--two { left: 800px; }
</style>
</head>
<body>
  <section class="cover cover--silhouette">
    <div class="cover__art" role="img" aria-label="Silhouette of a young man standing in a dim, backlit corridor"></div>
    <div class="cover__shade"></div>
    <h1 class="cover__title cover__title-top">Velvet</h1>
    <h2 class="cover__title cover__title-bottom">Mirror</h2>
    <p class="cover__tagline">DRAWN FROM REAL DAYS</p>
    <p class="cover__author">AUTHOR NAME</p>
  </section>

  <section class="cover cover--portrait">
    <div class="cover__art" role="img" aria-label="Black and white cropped portrait of a young man in a dark leather trench coat"></div>
    <h1 class="cover__title cover__title-top">Velvet</h1>
    <h2 class="cover__title cover__title-bottom">Mirror</h2>
    <p class="cover__tagline">DRAWN FROM REAL DAYS</p>
    <p class="cover__author">AUTHOR NAME</p>
  </section>

  <p class="option-label option-label--one">OPTION1</p>
  <p class="option-label option-label--two">OPTION2</p>
</body>
</html>
```